Number of Pages Required

1 page

Requirements
Must have
• An Overview / Background of the Business & Services(not for profit rescue animal farm)
• The Target Market / Audience you are trying to reach (animal lovers)
• Design Specifics; any preferences or ideas for Style, Colour, Imagery, etc (no preferences)

```html
<!DOCTYPE html>
<html lang="en">
<head>
<meta charset="utf-8">
<title>Stone Creek Farms</title>
<link href="https://fonts.googleapis.com/css2?family=Roboto+Slab:wght@300;400&family=Open+Sans:wght@400;600&display=swap" rel="stylesheet">
<style>
:root{
  --green:#3da53a;
  --green-dark:#1d6a1f;
  --nav-bg:rgba(20,50,15,.55);
  --ink:#444;
  --muted:#8a8a8a;
  --label:#333;
  --light:#f1f1f1;
  --footer:#1e1e1e;
  --white:#fff;
}
*{box-sizing:border-box;margin:0;padding:0}
html,body{width:1200px;height:3028px;overflow:hidden}
body{font-family:"Open Sans",sans-serif;color:var(--ink);background:var(--white)}
h1,h2,h3,.brand{font-family:"Roboto Slab",serif;font-weight:300}
.accent{color:var(--green)}

/* hero */
.hero{position:relative;height:740px;background:linear-gradient(180deg,#2f4a22 0%,#3e6a2a 35%,#5f9a38 60%,#3c6e23 85%,#24401a 100%)}
.nav{position:absolute;top:0;left:0;right:0;height:112px;background:var(--nav-bg);display:flex;align-items:center;justify-content:space-between;padding:0 112px}
.nav .brand{color:var(--white);font-size:30px;font-weight:400}
.nav ul{list-style:none;display:flex;gap:6px}
.nav a{display:block;color:var(--white);text-decoration:none;font-size:15px;padding:14px 22px}
.nav a.active{background:var(--green)}
.hero-text{position:absolute;top:196px;left:0;right:0;text-align:center;color:var(--white)}
.hero-text h1{font-size:66px;margin-bottom:26px}
.hero-text p{font-family:"Roboto Slab",serif;font-size:22px;line-height:1.45;width:640px;margin:0 auto}

/* welcome */
.welcome{height:600px;padding-top:58px;text-align:center}
.section-title{font-size:40px;color:#555}
.rule{width:54px;height:2px;background:var(--green);margin:18px auto 24px}
.intro{width:880px;margin:0 auto;font-size:13px;line-height:22px;color:var(--muted)}
.cards{display:flex;justify-content:center;gap:20px;margin-top:70px}
.card{width:312px}
.card .photo{height:230px}
.card .label{height:54px;background:var(--label);color:var(--white);font-size:16px;line-height:54px}

/* feature */
.feature{height:400px;display:flex;background:var(--green-dark)}
.feature .photo{width:540px;height:100%;background:linear-gradient(135deg,#8aa86a,#c9b49a 45%,#6f8a55)}
.feature .copy{flex:1;padding:60px 100px 0 40px;color:var(--white)}
.feature h3{font-size:28px;line-height:36px;margin-bottom:22px}
.feature p{font-size:12.5px;line-height:21px;color:#d7e8d4;width:500px}
.btn{display:inline-block;margin-top:28px;border:2px solid var(--white);border-radius:26px;color:var(--white);text-decoration:none;font-size:15px;padding:10px 28px}

/* gallery */
.gallery{height:660px;padding-top:50px;text-align:center}
.gallery .intro{width:auto}
.grid{display:grid;width:976px;margin:34px auto 0;grid-template-columns:280px 392px 288px;grid-template-rows:210px 210px;gap:8px}
.grid .g-big{grid-row:1 / span 2;grid-column:2}

/* testimonials */
.testimonials{height:400px;background:var(--light);padding-top:46px;text-align:center;position:relative}
.quote{position:relative;width:840px;margin:0 auto;font-size:13px;line-height:22px;color:var(--muted)}
.quote .mark{position:absolute;font-family:"Roboto Slab",serif;font-size:60px;color:#555;line-height:1}
.quote .open{left:-46px;top:-10px}
.quote .close{right:-46px;bottom:-34px}
.avatar{width:88px;height:88px;border-radius:50%;margin:28px auto 10px;border:4px solid var(--white);background:linear-gradient(180deg,#c9c9c9,#8c8c8c)}
.person{font-family:"Roboto Slab",serif;color:var(--green);font-size:18px}
.date{font-size:12px;color:var(--muted);margin-top:2px}

/* footer */
.footer{height:228px;background:var(--footer);color:#bbb;text-align:center;padding-top:54px}
.footer .brand{color:var(--white);font-size:46px}
.contact{display:flex;justify-content:center;gap:64px;margin-top:30px;font-size:13px}
.contact span{display:flex;align-items:center;gap:8px}
.contact svg{width:14px;height:14px;fill:#bbb}
.copyright{margin-top:22px;font-size:12px;color:#888}
</style>
</head>
<body>

<header class="hero" role="img" aria-label="Green farm pasture with grazing deer behind a wooden fence, framed by trees">
  <nav class="nav">
    <div class="brand">Stone Creek Farms</div>
    <ul>
      <li><a class="active" href="#">Home</a></li>
      <li><a href="#">About Us</a></li>
      <li><a href="#">Services</a></li>
      <li><a href="#">Store</a></li>
      <li><a href="#">Contact Us</a></li>
    </ul>
  </nav>
  <div class="hero-text">
    <h1>Stone Creek Farms</h1>
    <p>Sed ut perspiciatis unde omnis iste natus error sit voluptatem accusantium doloremque laudantium, totam rem aperiam</p>
  </div>
</header>

<section class="welcome">
  <h2 class="section-title">Welcome to <span class="accent">Stone Creek Farms</span></h2>
  <div class="rule"></div>
  <p class="intro">We are a not-for-profit farm giving a safe home to rescued animals. Horses, goats, cows, chickens and llamas live here with care, space and fresh pasture. Volunteers, families and animal lovers are welcome to visit, lend a hand, sponsor a resident or simply spend a quiet afternoon with the herd in the fields.</p>
  <div class="cards">
    <div class="card">
      <div class="photo" role="img" aria-label="Volunteers caring for animals outdoors" style="background:linear-gradient(135deg,#7fa35a,#b7a07c 55%,#5d7f3e)"></div>
      <div class="label">Non Profit Organization</div>
    </div>
    <div class="card">
      <div class="photo" role="img" aria-label="Open farm field under a bright sky" style="background:linear-gradient(180deg,#9bb9cf,#d8d3b8 45%,#6e8f3a 60%,#4d6f2a)"></div>
      <div class="label">Rescue Animal Farm</div>
    </div>
    <div class="card">
      <div class="photo" role="img" aria-label="Herd of cattle in a green pasture" style="background:linear-gradient(180deg,#c9d9e4,#8fb060 50%,#4d7a2e)"></div>
      <div class="label">Other</div>
    </div>
  </div>
</section>

<section class="feature">
  <div class="photo" role="img" aria-label="Mother and child meeting a llama at the farm"></div>
  <div class="copy">
    <h3>Sed ut perspiciatis unde omnis<br>iste natus error sit voluptatem accusantium</h3>
    <p>Every animal that arrives has a story. Some come from closed farms, others from neglect or owners who could no longer cope. Our team gives each one medical care, good food and patient handling until they feel at home. Your visits and gifts keep the barns warm, the pastures green and the gates open for the next rescue.</p>
    <a class="btn" href="#">Read More</a>
  </div>
</section>

<section class="gallery">
  <h2 class="section-title">Photo <span class="accent">Gallery</span></h2>
  <div class="rule"></div>
  <p class="intro">A glimpse of daily life on the farm with our rescued residents and friends.</p>
  <div class="grid">
    <div role="img" aria-label="Black and white cows grazing" style="background:linear-gradient(180deg,#a9c7df,#7fa64a 55%,#4f7a2a)"></div>
    <div class="g-big" role="img" aria-label="Hen and chicks on grass in sunlight" style="background:radial-gradient(circle at 40% 20%,#fffbe8,#d9d3b4 35%,#9fb56a 70%,#5c8a2c)"></div>
    <div role="img" aria-label="Sunset over a farm field" style="background:linear-gradient(180deg,#5d7ea6,#e7b968 50%,#6b7a3a 70%,#3d5322)"></div>
    <div role="img" aria-label="Cattle in a golden field" style="background:linear-gradient(180deg,#e8b070,#c98a4e 50%,#7a6a3a)"></div>
    <div role="img" aria-label="Cows resting in a barn yard" style="background:linear-gradient(135deg,#9a7a5c,#c7ad8d 50%,#5d4a38)"></div>
  </div>
</section>

<section class="testimonials">
  <h2 class="section-title">Our <span class="accent">Testimonials</span></h2>
  <div class="rule"></div>
  <div class="quote">
    <span class="mark open">&ldquo;</span>
    <p>Spending a Saturday at the farm was the highlight of our year. The staff knew every animal by name and let the children help at feeding time. It is clear how much love goes into this place, and we now sponsor a goat called Pepper. We will be back soon.</p>
    <span class="mark close">&rdquo;</span>
  </div>
  <div class="avatar" role="img" aria-label="Portrait of the reviewer"></div>
  <div class="person">Mara Ellison</div>
  <div class="date">Posted on 12 Feb 2016</div>
</section>

<footer class="footer">
  <div class="brand">Stone Creek Farms</div>
  <div class="contact">
    <span><svg viewBox="0 0 24 24"><path d="M6.6 10.8a15 15 0 0 0 6.6 6.6l2.2-2.2a1 1 0 0 1 1-.25 11.4 11.4 0 0 0 3.6.57 1 1 0 0 1 1 1V20a1 1 0 0 1-1 1A17 17 0 0 1 3 4a1 1 0 0 1 1-1h3.5a1 1 0 0 1 1 1c0 1.25.2 2.45.57 3.6a1 1 0 0 1-.25 1z"/></svg>Phone: 555-010-2468</span>
    <span><svg viewBox="0 0 24 24"><path d="M2 5h20v14H2zm2 2v.5l8 5 8-5V7zm0 2.9V17h16V9.9l-8 5z"/></svg>Email: hello@stonecreekfarms.org</span>
    <span><svg viewBox="0 0 24 24"><path d="M12 2a7 7 0 0 0-7 7c0 5 7 13 7 13s7-8 7-13a7 7 0 0 0-7-7zm0 9.5A2.5 2.5 0 1 1 12 6.5a2.5 2.5 0 0 1 0 5z"/></svg>KE/10 Lorem Ipsum, Country 1234 Lorem</span>
  </div>
  <p class="copyright">&copy; Copyright 2016 Stone Creek Farms all rights reserved</p>
</footer>

</body>
</html>
```